Brightmoor Leisure Works Investor Brochure

Start Up Company Brightmoor Leisure Works requires 4 page A4 size brochure outlining and detailing new product. Draft layout attached. Information and points of difference included. Company logo and graphics attached. Final design should sell to investors.
Industry/Entity Type
It Company

```html
<!DOCTYPE html>
<html lang="en">
<head>
<meta charset="utf-8">
<title>Brightmoor Leisure Works – Investor Brochure</title>
<link href="https://fonts.googleapis.com/css2?family=Roboto:ital,wght@0,300;0,400;0,700;1,400&display=swap" rel="stylesheet">
<style>
  :root {
    --stage: #2e2e2e;
    --brand-blue: #2f78bf;
    --brand-blue-dark: #1d5a9c;
    --brand-blue-deep: #123a6e;
    --accent-orange: #f6921e;
    --paper: #ffffff;
    --paper-grey: #eef0f2;
    --band-grey: #d9dcdf;
    --ink: #3d4852;
    --ink-soft: #6b7680;
    --rule: #dfe3e7;
  }
  * { box-sizing: border-box; margin: 0; padding: 0; }
  html, body { width: 1200px; height: 1000px; overflow: hidden; }
  body {
    background: var(--stage);
    font-family: "Roboto", Arial, sans-serif;
    color: var(--ink);
    position: relative;
  }
  .page { position: absolute; overflow: hidden; box-shadow: 0 4px 14px rgba(0,0,0,.45); }
  .placeholder { position: absolute; }

  /* ---------- page: exterior photo (back left) ---------- */
  .page-exterior { left: 40px; top: 365px; width: 430px; height: 600px; background: var(--paper); z-index: 1; }
  .page-exterior .photo-building {
    left: 0; top: 0; width: 100%; height: 165px;
    background: linear-gradient(180deg, #9fb2c4 0%, #c7ccd0 45%, #7f8a7a 75%, #6a6f6c 100%);
  }
  .page-exterior .title-band {
    position: absolute; left: 0; top: 165px; width: 100%; height: 100px;
    background: var(--brand-blue-dark); color: #fff; padding: 42px 0 0 120px; white-space: nowrap;
  }
  .page-exterior .title-band h2 { font-size: 17px; font-weight: 700; letter-spacing: 2px; }
  .page-exterior .title-band p { font-size: 12px; letter-spacing: 1px; margin-top: 4px; }

  /* ---------- page: hospitals (front left) ---------- */
  .page-hospitals { left: 40px; top: 630px; width: 422px; height: 370px; background: var(--paper); z-index: 2; }
  .page-hospitals .edge-strip { position: absolute; right: 0; top: 0; width: 12px; height: 100%; background: var(--brand-blue); }
  .hospitals-header {
    height: 30px; background: var(--brand-blue-dark); color: #fff;
    font-size: 8.5px; font-weight: 700; text-align: right; padding: 12px 50px 0 0; white-space: nowrap;
  }
  .page-hospitals .kiosk { left: 6px; top: 45px; width: 74px; height: 215px;
    background: linear-gradient(180deg, #3d7fc4, #1b4f8e); border-radius: 12px 6px 0 0; }
  .hospital-table { position: absolute; left: 84px; top: 42px; border-collapse: collapse; font-size: 6px; }
  .hospital-table th, .hospital-table td { height: 14.5px; border-bottom: 1px solid var(--rule); text-align: center; white-space: nowrap; }
  .hospital-table thead th { color: var(--ink-soft); font-weight: 400; width: 21px; height: 22px; }
  .hospital-table td { color: var(--ink-soft); border-left: 1px solid var(--rule); width: 21px; }
  .hospital-table th.row-label { width: 112px; text-align: right; padding-right: 6px; color: var(--brand-blue-dark); font-weight: 700; }
  .hospital-table tr.group th.row-label { color: var(--brand-blue-deep); }
  .brand-lockup { position: absolute; display: flex; align-items: center; gap: 8px; }
  .brand-lockup .mark { width: 26px; height: 26px; background: var(--ink-soft); flex: none; }
  .brand-lockup .name { font-weight: 700; letter-spacing: 1px; line-height: 1.05; white-space: nowrap; }
  .page-hospitals .brand-lockup { left: 148px; top: 228px; }
  .page-hospitals .brand-lockup .name { font-size: 14px; color: var(--brand-blue-dark); }
  .contact { position: absolute; left: 140px; top: 275px; width: 220px; text-align: center; font-size: 7px; color: var(--ink-soft); line-height: 1.7; font-style: normal; }

  /* ---------- page: cover ---------- */
  .page-cover { left: 180px; top: 33px; width: 432px; height: 607px; z-index: 3; }
  .page-cover .photo-terminal {
    left: 0; top: 0; width: 100%; height: 100%;
    background: linear-gradient(180deg, #1f4f95 0%, #3b6fb0 25%, #b9c9dc 45%, #d6dde4 65%, #aeb7c0 100%);
  }
  .page-cover .brand-lockup { left: 98px; top: 78px; }
  .page-cover .brand-lockup .mark { width: 40px; height: 40px; background: #fff; }
  .page-cover .brand-lockup .name { color: #fff; font-size: 22px; }
  .cover-band {
    position: absolute; left: 0; top: 466px; width: 100%; height: 100px;
    background: var(--brand-blue-dark); color: #fff; text-align: right; padding: 16px 24px 0 0; white-space: nowrap;
  }
  .cover-band h1 { font-size: 17px; font-weight: 700; letter-spacing: 1.5px; }
  .cover-band p { font-size: 12.5px; letter-spacing: .6px; margin-top: 4px; }
  .cover-band em { display: block; font-size: 10.5px; margin-top: 12px; }
  .page-cover .kiosk { left: 8px; top: 205px; width: 128px; height: 385px;
    background: linear-gradient(180deg, #3a7cc2, #1a4a87 70%, #222 100%); border-radius: 22px 10px 0 0; }

  /* ---------- shared section headers ---------- */
  .section-header { position: absolute; left: 0; top: 0; width: 100%; background: var(--brand-blue); color: #fff; text-align: center; white-space: nowrap; }
  .section-header .lead { font-size: 20px; font-weight: 700; letter-spacing: 3px; }
  .section-header .sub { font-size: 24px; font-weight: 300; letter-spacing: 5px; margin-top: 2px; }

  /* ---------- page: global expansion ---------- */
  .page-global { left: 549px; top: 612px; width: 431px; height: 400px; background: var(--paper-grey); z-index: 4; }
  .page-global .section-header { height: 84px; padding-top: 26px; }
  .page-global .section-header .lead, .page-global .section-header .sub { font-size: 22px; letter-spacing: 4px; }
  .page-global .section-header .lead { font-weight: 400; }
  .page-global .map-world { left: 12px; top: 105px; width: 410px; height: 185px;
    background: radial-gradient(ellipse at 50% 50%, #3f83c8 0%, #3b7cc0 60%, #5c93cc 100%); border-radius: 40px; opacity: .9; }
  .stat-line { position: absolute; left: 0; top: 312px; width: 100%; text-align: center; font-size: 9.5px; font-weight: 700; color: var(--accent-orange); white-space: nowrap; }
  .wifi-box { position: absolute; left: 18px; top: 338px; width: 395px; height: 60px; background: var(--brand-blue-dark); color: #fff; text-align: center; padding-top: 14px; }
  .wifi-box h4 { font-size: 10.5px; font-weight: 400; letter-spacing: .5px; }
  .wifi-box p { font-size: 6.5px; margin-top: 4px; }

  /* ---------- page: Australian airports (front right) ---------- */
  .page-australia { left: 668px; top: 33px; width: 430px; height: 607px; background: var(--paper-grey); z-index: 5; }
  .page-australia .section-header { height: 95px; padding-top: 24px; }
  .page-australia .map-australia { left: 212px; top: 118px; width: 200px; height: 160px;
    background: radial-gradient(ellipse at 55% 45%, #4d8fd0, #3b7cc0 68%, var(--paper-grey) 70%); }
  .page-australia .kiosk { left: 6px; top: 145px; width: 150px; height: 385px;
    background: linear-gradient(180deg, #2f6fb6, #163f78 80%, #1c1c1c 100%); border-radius: 28px 10px 0 0; }
  .airport-panel { position: absolute; left: 144px; top: 276px; width: 264px; background: #fff; box-shadow: 0 1px 4px rgba(0,0,0,.15); }
  .airport-panel header { background: var(--brand-blue-dark); color: #fff; text-align: center; padding: 7px 0 6px; }
  .airport-panel header h3 { font-size: 9px; font-weight: 700; }
  .airport-panel header p { font-size: 5.5px; margin-top: 2px; }
  .airport-table { width: 100%; border-collapse: collapse; font-size: 5.5px; margin-top: 6px; }
  .airport-table td { height: 15px; border-bottom: 1px solid var(--rule); white-space: nowrap; }
  .airport-table tr:nth-child(even) td { background: #f5f6f7; }
  .airport-table .city { text-align: right; color: var(--brand-blue-dark); padding-right: 8px; width: 30%; }
  .airport-table .count { color: var(--ink-soft); padding-left: 8px; width: 20%; }
  .airport-panel footer { background: var(--accent-orange); color: #fff; font-size: 10px; padding: 6px 0 6px 70px; margin-top: 4px; white-space: nowrap; }
  .airport-panel footer strong { font-weight: 700; }
  .points-band { position: absolute; left: 0; top: 532px; width: 100%; height: 75px; background: var(--band-grey); padding: 8px 12px 0 48px; }
  .points-band li { list-style: none; font-size: 7px; line-height: 9px; color: var(--ink); margin-bottom: 6px; position: relative; white-space: nowrap; }
  .points-band li::before { content: ""; position: absolute; left: -12px; top: 1px; border-left: 6px solid var(--brand-blue); border-top: 3px solid transparent; border-bottom: 3px solid transparent; }
  .points-band li strong { display: block; font-weight: 700; margin-top: 1px; }
</style>
</head>
<body>

<!-- exterior page -->
<section class="page page-exterior">
  <div class="placeholder photo-building" role="img" aria-label="Photograph of an airport terminal exterior with parked cars under a cloudy sky"></div>
  <div class="title-band">
    <h2>MOVIES FOR TRAVELLERS</h2>
    <p>DOWNLOAD MOVIES IN UNDER 3 MINUTES</p>
  </div>
</section>

<!-- hospitals page -->
<section class="page page-hospitals">
  <div class="hospitals-header">PUBLIC AND PRIVATE HOSPITALS, STATES AND TERRITORIES, 2012-13</div>
  <div class="placeholder kiosk" role="img" aria-label="Product render of the blue movie download kiosk"></div>
  <table class="hospital-table">
    <thead>
      <tr><th class="row-label"></th><th>NSW</th><th>Vic</th><th>Qld</th><th>WA</th><th>SA</th><th>Tas</th><th>ACT</th><th>NT</th><th>Total</th></tr>
    </thead>
    <tbody>
      <tr class="group"><th class="row-label">PUBLIC HOSPITALS</th><td></td><td></td><td></td><td></td><td></td><td></td><td></td><td></td><td></td></tr>
      <tr><th class="row-label">PUBLIC ACUTE HOSPITALS</th><td>218</td><td>218</td><td>218</td><td>218</td><td>218</td><td>218</td><td>218</td><td>218</td><td>218</td></tr>
      <tr><th class="row-label">PUBLIC PSYCHIATRIC HOSPITALS</th><td>7</td><td>7</td><td>7</td><td>7</td><td>7</td><td>7</td><td>7</td><td>7</td><td>7</td></tr>
      <tr><th class="row-label">TOTAL PUBLIC HOSPITALS</th><td>225</td><td>225</td><td>225</td><td>225</td><td>225</td><td>225</td><td>225</td><td>225</td><td>225</td></tr>
      <tr class="group"><th class="row-label">PRIVATE HOSPITALS</th><td></td><td></td><td></td><td></td><td></td><td></td><td></td><td></td><td></td></tr>
      <tr><th class="row-label">PRIVATE FREE-STANDING DAY</th><td>96</td><td>96</td><td>96</td><td>96</td><td>96</td><td>96</td><td>96</td><td>96</td><td>96</td></tr>
      <tr><th class="row-label">OTHER PRIVATE HOSPITALS</th><td>89</td><td>89</td><td>89</td><td>89</td><td>89</td><td>89</td><td>89</td><td>89</td><td>89</td></tr>
      <tr><th class="row-label">TOTAL PRIVATE HOSPITALS</th><td>185</td><td>185</td><td>185</td><td>185</td><td>185</td><td>185</td><td>185</td><td>185</td><td>185</td></tr>
      <tr class="group"><th class="row-label">ALL HOSPITALS</th><td>410</td><td>410</td><td>410</td><td>410</td><td>410</td><td>410</td><td>410</td><td>410</td><td>410</td></tr>
    </tbody>
  </table>
  <div class="brand-lockup">
    <span class="mark"></span>
    <span class="name">BRIGHTMOOR<br>LEISURE WORKS</span>
  </div>
  <address class="contact">
    #12 Street name,<br>City Name 123 456, Country<br>+1 555 0142<br>hello@brightmoorworks.com
  </address>
  <div class="edge-strip"></div>
</section>

<!-- cover page -->
<section class="page page-cover">
  <div class="placeholder photo-terminal" role="img" aria-label="Photograph of a bright airport terminal concourse with travellers and departure boards"></div>
  <div class="brand-lockup">
    <span class="mark"></span>
    <span class="name">BRIGHTMOOR<br>LEISURE WORKS</span>
  </div>
  <div class="cover-band">
    <h1>MOVIES FOR TRAVELLERS</h1>
    <p>DOWNLOAD MOVIES IN UNDER 3 MINUTES</p>
    <em>No internet Connection Required.</em>
  </div>
  <div class="placeholder kiosk" role="img" aria-label="Product render of the curved blue movie download kiosk"></div>
</section>

<!-- global page -->
<section class="page page-global">
  <header class="section-header">
    <div class="lead">TECHNOLOGY BUILT FOR</div>
    <div class="sub">GLOBAL EXPANSION</div>
  </header>
  <div class="placeholder map-world" role="img" aria-label="World map in blue"></div>
  <p class="stat-line">TOP 20 AIRPORTS IN THE WORLD EXCEEDED 1.2 BILLION PASSENGERS IN 2013</p>
  <div class="wifi-box">
    <h4>INCORPORATING BLAZING FAST WIFI</h4>
    <p>(Future Devices to Download SD Movies in a few seconds)</p>
  </div>
</section>

<!-- Australia page -->
<section class="page page-australia">
  <header class="section-header">
    <div class="lead">COMING SOON TO AIRPORTS</div>
    <div class="sub">ACROSS AUSTRALIA</div>
  </header>
  <div class="placeholder map-australia" role="img" aria-label="Map of Australia marking airport locations"></div>
  <div class="placeholder kiosk" role="img" aria-label="Product render of the curved blue movie download kiosk"></div>
  <div class="airport-panel">
    <header>
      <h3>145,000,000+ PASSENGER MOVEMENTS</h3>
      <p>New Airport announced for Western Sydney to cope with increase demand</p>
    </header>
    <table class="airport-table">
      <tr><td class="city">SYDNEY</td><td class="count">38 437 737</td><td class="city">MELBOURNE</td><td class="count">30 484 074</td></tr>
      <tr><td class="city">BRISBANE</td><td class="count">21 570 625</td><td class="city">PERTH</td><td class="count">12 989 955</td></tr>
      <tr><td class="city">ADELAIDE</td><td class="count">7 460 471</td><td class="city">GOLD COAST</td><td class="count">5 789 986</td></tr>
      <tr><td class="city">CAIRNS</td><td class="count">4 293 485</td><td class="city">CANBERRA</td><td class="count">2 931 006</td></tr>
      <tr><td class="city">HOBART</td><td class="count">2 098 416</td><td class="city">DARWIN</td><td class="count">2 023 665</td></tr>
      <tr><td class="city">TOWNSVILLE</td><td class="count">1 543 457</td><td class="city">LAUNCESTON</td><td class="count">1 267 589</td></tr>
      <tr><td class="city">WILLIAMTOWN</td><td class="count">1 208 188</td><td class="city">MACKAY</td><td class="count">1 083 805</td></tr>
      <tr><td class="city">SUNSHINE COAST</td><td class="count">891 300</td><td class="city">KARRATHA</td><td class="count">783 137</td></tr>
      <tr><td class="city">ROCKHAMPTON</td><td class="count">694 368</td><td class="city">ALICE SPRINGS</td><td class="count">667 383</td></tr>
      <tr><td class="city">GLADSTONE</td><td class="count">500 429</td><td class="city">PORT HEDLAND</td><td class="count">491 274</td></tr>
    </table>
    <footer>FOR YE FEB 2014. <strong>UP 3.1% ON 2013</strong></footer>
  </div>
  <ul class="points-band">
    <li>Current technology allows up to 10,000 encrypted digital movies to be stored on a kiosk.</li>
    <li>Multiple customers can simultaneously browse and rent movies on the Kiosks FREE Wifi.</li>
    <li>Travellers are always killing time waiting to board there flight. Perfect time to browse movies.<strong>Target of 1 million transactions in the first 12 months</strong></li>
  </ul>
</section>

</body>
</html>
```